Staffing and Consulting Service Company needs Business Cards

We need to have business cards for our business. You can check our website www.quelbrantix.com to see the branding we are using. The logo is in the website.
We use a tag line Staffing & Consulting Solutions Made Easy.
We use different blues in the logo and we use the red for the Company name.
As you can see in the website there is a gradient in the bottom part of each page that includes some of the dots we use for the logo.
We will need the following fields on the design:
Company Name
Employee Name
Title
Address
Tel
Email
Website
Can be Single or Double Sided
There is no preference for single or double sided.
Target Market(s)
Companies in need of IT staffing and IT consulting services
Industry/Entity Type
Business
Look and feel

```html
<!DOCTYPE html>
<html lang="en">
<head>
<meta charset="utf-8">
<title>Quelbrantix Business Card</title>
<link rel="stylesheet" href="https://fonts.googleapis.com/css2?family=Tinos&family=Didact+Gothic&display=swap">
<style>
  :root {
    --page-bg: #e6e6ea;
    --card-white: #ffffff;
    --card-shade: #ececee;
    --brand-red: #c8202b;
    --brand-navy: #1e2657;
    --ink: #1b1b1f;
    --dot-grey: #e2e2e5;
  }
  * { margin: 0; padding: 0; box-sizing: border-box; }
  html, body {
    width: 1200px; height: 800px; overflow: hidden;
    background: var(--page-bg);
  }
  .card {
    position: absolute; left: 100px; top: 114px;
    width: 1000px; height: 572px;
    background: linear-gradient(180deg, var(--card-shade) 0%, var(--card-white) 42%, var(--card-white) 100%);
    box-shadow: 0 10px 30px rgba(0,0,0,.18);
    overflow: hidden;
    font-family: "Didact Gothic", "Century Gothic", sans-serif;
    color: var(--ink);
  }
  .brand-mark {
    position: absolute; left: 70px; top: 104px;
    width: 168px; height: 168px;
    background: var(--brand-navy); border-radius: 16px;
  }
  .brand-name {
    position: absolute; left: 260px; top: 112px;
    max-width: 680px;
    font-family: "Tinos", "Times New Roman", serif;
    font-size: 82px; line-height: 1; letter-spacing: 0;
    color: var(--brand-red);
    white-space: nowrap;
  }
  .tagline-band {
    position: absolute; left: 0; top: 282px; width: 100%; height: 30px;
    background: var(--brand-navy);
  }
  .tagline {
    position: absolute; left: 70px; top: 3px;
    font-size: 20px; letter-spacing: 7.2px; color: var(--card-white);
    white-space: nowrap;
  }
  .backdrop-fade {
    position: absolute; right: 0; top: 312px; width: 420px; height: 260px;
    background: radial-gradient(ellipse at 60% 40%, var(--dot-grey) 0%, rgba(255,255,255,0) 70%);
  }
  .person { position: absolute; left: 70px; top: 322px; }
  .person-name { font-size: 34px; color: var(--brand-red); letter-spacing: .5px; -webkit-text-stroke: .8px var(--brand-red); }
  .person-title { font-size: 21px; margin-left: 16px; margin-top: -2px; }
  .contacts { position: absolute; left: 86px; top: 408px; list-style: none; }
  .contacts li {
    display: flex; align-items: center; gap: 10px;
    font-size: 31px; line-height: 38px; white-space: nowrap;
  }
  .contacts svg { width: 28px; height: 28px; flex: none; fill: var(--brand-red); }
</style>
</head>
<body>
  <div class="card">
    <div class="brand-mark"></div>
    <div class="brand-name">QUELBRANTIX</div>
    <div class="tagline-band">
      <div class="tagline">Staffing &amp; Consulting Solutions Made Easy</div>
    </div>
    <div class="backdrop-fade" role="img" aria-label="Faint grey brand dot pattern fading out"></div>
    <div class="person">
      <div class="person-name">Dana Whitfield</div>
      <div class="person-title">Manager</div>
    </div>
    <ul class="contacts">
      <li>
        <svg viewBox="0 0 24 24" aria-hidden="true"><path d="M6.6 10.8a15.1 15.1 0 0 0 6.6 6.6l2.2-2.2c.3-.3.7-.4 1-.2 1.1.4 2.3.6 3.6.6.6 0 1 .4 1 1V20c0 .6-.4 1-1 1A17 17 0 0 1 3 4c0-.6.4-1 1-1h3.5c.6 0 1 .4 1 1 0 1.3.2 2.5.6 3.6.1.3 0 .7-.2 1z"/></svg>
        <span>(954) 555-0137</span>
      </li>
      <li>
        <svg viewBox="0 0 24 24" aria-hidden="true"><path d="M12 2a10 10 0 1 0 0 20 10 10 0 0 0 0-20zm6.9 6h-3a15.6 15.6 0 0 0-1.4-3.6A8 8 0 0 1 18.9 8zM12 4c.8 1.2 1.5 2.5 1.9 4h-3.8c.4-1.5 1.1-2.8 1.9-4zM4.3 14a8 8 0 0 1 0-4h3.4a16.5 16.5 0 0 0 0 4zm.8 2h3a15.6 15.6 0 0 0 1.4 3.6A8 8 0 0 1 5.1 16zm3-8h-3a8 8 0 0 1 4.4-3.6C8.9 5.5 8.4 6.7 8.1 8zM12 20c-.8-1.2-1.5-2.5-1.9-4h3.8c-.4 1.5-1.1 2.8-1.9 4zm2.3-6H9.7a14.7 14.7 0 0 1 0-4h4.6a14.7 14.7 0 0 1 0 4zm.2 5.6c.6-1.1 1.1-2.3 1.4-3.6h3a8 8 0 0 1-4.4 3.6zm1.8-5.6a16.5 16.5 0 0 0 0-4h3.4a8 8 0 0 1 0 4z"/></svg>
        <span>www.quelbrantix.com</span>
      </li>
      <li>
        <svg viewBox="0 0 24 24" aria-hidden="true"><path d="M2 5h20v14H2zm2 2v.5l8 5 8-5V7zm0 2.8V17h16V9.8l-8 5z"/></svg>
        <span>dana@quelbrantix.com</span>
      </li>
      <li>
        <svg viewBox="0 0 24 24" aria-hidden="true"><path d="M12 3 1 12h3v9h6v-6h4v6h6v-9h3z"/></svg>
        <span>4410 NW 88th Lane Sunrise, FL 33351</span>
      </li>
    </ul>
  </div>
</body>
</html>
```